Voltline Assemblies, Inc. Business Card

Voltline has three operating entities and I'm looking for a standard business card template that can be used for Voltline and the three operating entities that the logo just get swapped out, but has a very similar look and feel. Ultimately if someone had a business card from each, they assume the organizations are related because they all have the same look and feel.
Below are our websites and I will attached the logos for each entity:
https://www.voltlineassemblies.example/
https://www.brantoceramic.example/
https://www.omra-kfsd.example/
https://www.summitbreaker.example/

Target Market(s)

US Voltline

Industry/Entity Type

US Voltline

Contact Information for Business Card

Normal stuff

```html
<!DOCTYPE html>
<html lang="en">
<head>
<meta charset="utf-8">
<title>Voltline Assemblies, Inc. Business Card</title>
<link href="https://fonts.googleapis.com/css2?family=Poppins:wght@400;500;600;700&display=swap" rel="stylesheet">
<style>
  :root {
    --navy: #22306a;
    --navy-faint: #2b3a78;
    --red: #c8202f;
    --white: #ffffff;
    --ink: #1f2233;
    --backdrop: #c9c9cb;
    --mark-faint: #eceef3;
  }
  * { box-sizing: border-box; margin: 0; padding: 0; }
  html, body {
    width: 1200px; height: 852px; overflow: hidden;
    background: var(--backdrop);
    font-family: "Poppins", sans-serif;
  }
  .stage { position: relative; width: 1200px; height: 852px; }

  .card {
    position: absolute;
    width: 560px; height: 320px;
    border-radius: 18px;
    overflow: hidden;
  }

  /* Back of card */
  .card-back { left: 50px; top: 90px; background: var(--navy); }
  .card-back .faint-circle {
    position: absolute; right: -40px; top: -60px;
    width: 300px; height: 300px; border-radius: 50%;
    background: var(--navy-faint);
  }
  .card-back .brand {
    position: absolute; left: 0; right: 0; top: 112px;
    display: flex; align-items: center; justify-content: center; gap: 12px;
  }
  .card-back .brand-dot {
    width: 34px; height: 34px; border-radius: 50%; background: var(--white);
  }
  .card-back .brand-name {
    color: var(--white); font-weight: 700; font-size: 26px; letter-spacing: 0.5px;
  }
  .card-back .website {
    position: absolute; left: 0; right: 0; bottom: 44px; text-align: center;
    color: var(--white); font-weight: 500; font-size: 13px; letter-spacing: 4px;
  }

  /* Front of card */
  .card-front { left: 590px; top: 440px; background: var(--white); }
  .card-front .faint-circle {
    position: absolute; right: -20px; top: -40px;
    width: 230px; height: 230px; border-radius: 50%;
    background: var(--mark-faint);
  }
  .card-front .brand {
    position: absolute; right: 34px; top: 34px;
    display: flex; align-items: center; gap: 10px;
  }
  .card-front .brand-dot {
    width: 30px; height: 30px; border-radius: 50%; background: var(--navy);
  }
  .card-front .brand-name {
    color: var(--navy); font-weight: 700; font-size: 17px;
  }
  .edge-tab-red {
    position: absolute; left: 0; top: 128px; width: 10px; height: 40px; background: var(--red);
  }
  .edge-bar-navy {
    position: absolute; right: 0; bottom: 0; width: 140px; height: 16px; background: var(--navy);
  }
  .person { position: absolute; left: 36px; top: 112px; }
  .person-name { color: var(--navy); font-weight: 700; font-size: 22px; line-height: 1.15; }
  .person-title { color: var(--red); font-weight: 500; font-size: 14px; }

  .rule-red {
    position: absolute; left: 36px; top: 184px; width: 260px; height: 2px; background: var(--red);
  }
  .rule-navy {
    position: absolute; left: 310px; top: 104px; width: 216px; height: 2px; background: var(--navy);
  }
  .address {
    position: absolute; right: 34px; top: 114px; text-align: right;
    color: var(--ink); font-size: 12.5px; line-height: 1.5;
  }
  .contacts {
    position: absolute; left: 36px; top: 200px; list-style: none;
  }
  .contacts li {
    display: flex; align-items: center; gap: 10px;
    color: var(--ink); font-size: 13px; line-height: 1.6;
  }
  .contacts svg { width: 12px; height: 12px; fill: var(--red); flex: none; }
</style>
</head>
<body>
<main class="stage">

  <section class="card card-back" aria-label="Card back">
    <div class="faint-circle"></div>
    <div class="brand">
      <span class="brand-dot"></span>
      <span class="brand-name">Voltline Assemblies, Inc.</span>
    </div>
    <p class="website">WWW.VOLTLINEASSEMBLIES.EXAMPLE</p>
  </section>

  <section class="card card-front" aria-label="Card front">
    <div class="faint-circle"></div>
    <div class="edge-tab-red"></div>
    <div class="edge-bar-navy"></div>

    <div class="brand">
      <span class="brand-dot"></span>
      <span class="brand-name">Voltline Assemblies, Inc.</span>
    </div>

    <div class="rule-navy"></div>
    <p class="address">2740 Ridgecrest Drive, Suite 210<br>Marlow, AL 35990</p>

    <div class="person">
      <h1 class="person-name">Dale Whitford</h1>
      <p class="person-title">CEO / Board Member</p>
    </div>

    <div class="rule-red"></div>

    <ul class="contacts">
      <li>
        <svg viewBox="0 0 24 24" aria-hidden="true"><path d="M6.6 10.8a15 15 0 0 0 6.6 6.6l2.2-2.2c.3-.3.7-.4 1-.2 1.1.4 2.3.6 3.6.6.6 0 1 .4 1 1V20c0 .6-.4 1-1 1A17 17 0 0 1 3 4c0-.6.4-1 1-1h3.5c.6 0 1 .4 1 1 0 1.3.2 2.5.6 3.6.1.3 0 .7-.2 1z"/></svg>
        555-0134-2211
      </li>
      <li>
        <svg viewBox="0 0 24 24" aria-hidden="true"><path d="M7 1h10a2 2 0 0 1 2 2v18a2 2 0 0 1-2 2H7a2 2 0 0 1-2-2V3a2 2 0 0 1 2-2zm0 3v14h10V4zm5 15.5a1 1 0 1 0 0 2 1 1 0 0 0 0-2z"/></svg>
        555-0187-4420
      </li>
      <li>
        <svg viewBox="0 0 24 24" aria-hidden="true"><path d="M2 5h20v14H2zm2 2v.5l8 5 8-5V7zm0 2.9V17h16V9.9l-8 5z"/></svg>
        info@omra-kfsd.example
      </li>
      <li>
        <svg viewBox="0 0 24 24" aria-hidden="true"><path d="M12 2a10 10 0 1 0 0 20 10 10 0 0 0 0-20zm6.9 9h-3a15 15 0 0 0-1.3-5.4A8 8 0 0 1 18.9 11zM12 4c.9 1.2 1.7 3.7 1.9 7h-3.8c.2-3.3 1-5.8 1.9-7zM9.4 5.6A15 15 0 0 0 8.1 11h-3a8 8 0 0 1 4.3-5.4zM5.1 13h3a15 15 0 0 0 1.3 5.4A8 8 0 0 1 5.1 13zm6.9 7c-.9-1.2-1.7-3.7-1.9-7h3.8c-.2 3.3-1 5.8-1.9 7zm2.6-1.6a15 15 0 0 0 1.3-5.4h3a8 8 0 0 1-4.3 5.4z"/></svg>
        www.omra-kfsd.example
      </li>
    </ul>
  </section>

</main>
</body>
</html>
```